Web Design Project for Communications Agency

The design I need (PSD file) is for an agency offering specialised PR and communications services for customers in the healthcare sector.

OBJECTIVES OF THE WEBSITE:
1. To promote the agency's communication services
2. To position Solène Verbruggen as an industry leader, an expert in healthcare PR and communications by highlighting blogposts and social media.

WHAT I NEED:
1st, I need the design for the Home Page ONLY.
Once approved, I will need the other pages designed as well. (Here is prototype that we've already developed for the Website that will guide you in the design:
http://qoravenlab.com/solenverbruggen/)

VISUAL INSPIRATION
We want to give this Website a "Flat Design" look. Here are some websites for inspiration :
- http://lumbrafolk.com/#!/process
- http://www.quillmarsh.co/
- http://dorvellink.com/

Also, reuse images found on the company's current Website :
http://www.solenverbruggen.com/fr/index.html

HOMEPAGE MAIN ELEMENTS:
1. Main menu : 6 sections
Accueil | Agence | Services | Approche | Publications | Contact

2. Main Call To Action (big dark rectangle in prototype):
Can be slider or just an information bloc.

3. Publications récentes :
The 4 latest blog posts must be features on the homepage (will be linked with the "Publications" section)

4. Dynamic Footer :
Contains a Chirpline feed and a Subscribe to our Newsletter feature (revecez nos publications)

OTHER PAGES (to design once Homepage is approved)
- Agence (about us)
- Services (our team)
- Approche (our approach)
- Publications (blog articles)
- Contact (Contact us)

• Please refer to prototype :
http://qoravenlab.com/solenverbruggen/
Must have ALL features present in prototype.

Also, must reuse this picture in the design : http://solenverbruggen.com/static/images/home-big-box.jpg

Finally, you will find attached the company logo.

```html
<!DOCTYPE html>
<html lang="fr">
<head>
<meta charset="utf-8">
<title>Solène Verbruggen — Gestion d'enjeux, affaires publiques</title>
<link rel="stylesheet" href="https://fonts.googleapis.com/css2?family=Open+Sans:ital,wght@0,300;0,400;0,600;0,700;1,400&family=Gelasio:ital,wght@0,400;1,400&display=swap">
<style>
  :root {
    --red: #c8141c;
    --red-dark: #a50d13;
    --ink: #222;
    --text: #555;
    --muted: #8a8a8a;
    --page: #f2f3f2;
    --card-alt: #f2f2f2;
    --footer: #222;
    --line: #e3e3e3;
    --social: #c9c9c9;
    --chirp: #2a9fd8;
  }
  * { box-sizing: border-box; margin: 0; padding: 0; }
  html, body { width: 1200px; height: 2264px; overflow: hidden; }
  body { position: relative; font-family: "Open Sans", Arial, sans-serif; color: var(--text); background: var(--page); }

  .site-header { position: absolute; left: 0; top: 0; width: 1200px; height: 125px; background: #fff; border-top: 2px solid #333; }
  .brand { position: absolute; left: 116px; top: 38px; display: flex; align-items: center; gap: 14px; }
  .brand-mark { width: 22px; height: 22px; background: var(--red); }
  .brand-name { font-size: 30px; font-weight: 600; color: var(--red); letter-spacing: -0.5px; }
  .brand-tagline { position: absolute; left: 152px; top: 82px; font-size: 11px; font-weight: 600; color: #666; letter-spacing: 1px; line-height: 13px; }
  .lang { position: absolute; left: 981px; top: 4px; width: 110px; height: 28px; background: #e6e6e6; padding: 4px 8px; }
  .lang-select { display: flex; align-items: center; height: 20px; border: 1px solid #999; background: #fff; font-size: 12px; color: var(--red); }
  .lang-select span { padding: 0 4px; flex: 1; }
  .lang-flag { width: 14px; height: 9px; background: #3a4d8f; margin-right: 4px; }
  .lang-arrow { width: 16px; height: 18px; border-left: 1px solid #999; background: #ddd; position: relative; }
  .lang-arrow::after { content: ""; position: absolute; left: 4px; top: 7px; border: 4px solid transparent; border-top-color: #333; }
  .social { position: absolute; left: 945px; top: 63px; display: flex; gap: 7px; }
  .social-dot { width: 24px; height: 24px; border-radius: 50%; background: var(--social); }

  .main-nav { position: absolute; left: 0; top: 125px; width: 1200px; height: 41px; background: linear-gradient(#d7242b, var(--red-dark)); }
  .main-nav ul { list-style: none; display: flex; padding-left: 107px; height: 41px; }
  .main-nav li { font-size: 13px; color: #fff; line-height: 41px; padding: 0 19px; border-right: 1px solid rgba(0,0,0,.18); box-shadow: 1px 0 0 rgba(255,255,255,.15); }
  .main-nav li:last-child { border: 0; box-shadow: none; }

  .hero { position: absolute; left: 0; top: 166px; width: 1200px; height: 408px; }
  .hero-backdrop { position: absolute; inset: 0; background: linear-gradient(180deg, #f4f4f4 0%, #e8e8e8 45%, #d7d5d3 100%); }
  .hero-visual { position: absolute; left: 717px; top: 38px; width: 362px; height: 347px; background: radial-gradient(circle at 45% 40%, #fafafa 0%, #e6e6e6 55%, rgba(200,20,28,.25) 100%); }
  .hero-title { position: absolute; left: 112px; top: 92px; width: 560px; font-size: 29px; font-weight: 600; line-height: 36px; color: var(--ink); }
  .hero-cta { position: absolute; left: 112px; top: 226px; width: 288px; height: 71px; background: linear-gradient(#2e2e2e, #121212); border-radius: 3px; display: flex; align-items: center; }
  .hero-cta-icon { position: absolute; left: -2px; top: 14px; width: 42px; height: 42px; background: var(--red); display: flex; align-items: center; justify-content: center; }
  .hero-cta-label { margin-left: 60px; font-size: 23px; font-weight: 700; color: #fff; }

  .section-title { position: absolute; left: 454px; top: 623px; width: 303px; height: 61px; background: #fff; border-bottom: 4px solid var(--red); font-size: 30px; font-weight: 400; color: #333; text-align: center; line-height: 58px; }

  .site-footer { position: absolute; left: 0; top: 1906px; width: 1200px; height: 358px; background: var(--footer); }

  .posts { position: absolute; left: 121px; top: 732px; width: 961px; box-shadow: 0 0 6px rgba(0,0,0,.1); }
  .post { height: 305px; padding: 30px 40px 0 36px; background: #fff; border-bottom: 1px solid var(--line); }
  .post:nth-child(2) { height: 307px; }
  .post:nth-child(even) { background: var(--card-alt); }
  .post:last-child { border-bottom: 0; height: 304px; }
  .post-media { float: left; width: 230px; height: 130px; margin: 0 25px 14px 0; }
  .media-lab { background: linear-gradient(135deg, #c7dcd8, #8fb0ab 60%, #dfe9e7); }
  .media-flask { background: linear-gradient(135deg, #9fc6e0, #e8eef2 50%, #d8c27a); }
  .media-cross { background: linear-gradient(135deg, #f1f1f1, #d7d7d7 50%, #cc3a40); }
  .media-doctors { background: linear-gradient(135deg, #eef2f6, #b9c7d6 55%, #6f87a6); }
  .post-title { font-family: "Gelasio", Georgia, serif; font-size: 17px; color: var(--ink); margin-top: 6px; }
  .post-date { display: inline-block; margin-top: 6px; padding: 4px 6px; background: var(--card-alt); font-family: "Gelasio", Georgia, serif; font-style: italic; font-size: 15px; color: var(--ink); }
  .post:nth-child(even) .post-date { background: #fff; }
  .post-excerpt { margin-top: 16px; font-size: 12.4px; line-height: 18px; color: var(--text); }
  .post-excerpt em { font-style: normal; color: var(--red); }
  .post-more { clear: both; display: inline-flex; align-items: center; gap: 10px; margin-top: 16px; padding: 0 14px; height: 35px; background: var(--card-alt); font-size: 13.5px; color: var(--red); }
  .post:nth-child(even) .post-more { background: #fff; }

  .feed { position: absolute; left: 116px; top: 1998px; width: 430px; }
  .feed-name { display: flex; align-items: center; gap: 12px; font-size: 40px; font-weight: 700; color: var(--chirp); line-height: 48px; }
  .feed-dot { width: 16px; height: 16px; border-radius: 50%; background: var(--chirp); }
  .feed-text { margin-top: 10px; font-size: 11.5px; line-height: 15px; color: #fff; }
  .feed-tags { margin-top: 6px; font-size: 11.5px; color: #fff; word-spacing: 14px; }
  .feed-button { margin-top: 12px; width: 79px; height: 30px; background: linear-gradient(#3a9fe0, #2a83c6); border-radius: 3px; color: #fff; font-size: 14px; font-weight: 600; text-align: center; line-height: 30px; }

  .newsletter { position: absolute; left: 798px; top: 2000px; width: 290px; }
  .newsletter-title { font-size: 19px; font-weight: 600; color: #fff; }
  .newsletter-field { width: 275px; height: 34px; margin-top: 14px; background: #fff; border-radius: 2px; padding: 0 12px; font-size: 14.5px; line-height: 34px; color: #999; }
  .newsletter-field + .newsletter-field { margin-top: 12px; }
  .newsletter-submit { width: 160px; height: 34px; margin-top: 12px; background: linear-gradient(#d41a22, var(--red-dark)); color: #fff; font-size: 15px; font-weight: 600; text-align: center; line-height: 34px; }

  .footer-rule { position: absolute; left: 112px; top: 2199px; width: 976px; height: 1px; background: #3a3a3a; }
  .copyright { position: absolute; left: 112px; top: 2213px; font-size: 12px; color: #ccc; }
</style>
</head>
<body>
  <header class="site-header">
    <div class="brand"><span class="brand-mark"></span><span class="brand-name">Solène Verbruggen</span></div>
    <div class="brand-tagline">GESTION D'ENJEUX · AFFAIRES PUBLIQUES</div>
    <div class="lang"><div class="lang-select"><span>English</span><i class="lang-flag"></i><i class="lang-arrow"></i></div></div>
    <div class="social">
      <span class="social-dot"></span><span class="social-dot"></span><span class="social-dot"></span><span class="social-dot"></span>
      <svg width="24" height="24" viewBox="0 0 24 24" aria-label="Recherche"><circle cx="12" cy="12" r="12" fill="#c9c9c9"/><circle cx="11" cy="11" r="4.5" fill="none" stroke="#fff" stroke-width="2"/><line x1="14.2" y1="14.2" x2="17.5" y2="17.5" stroke="#fff" stroke-width="2.4" stroke-linecap="round"/></svg>
    </div>
  </header>

  <nav class="main-nav">
    <ul><li>ACCUEIL</li><li>AGENCE</li><li>SERVICES</li><li>APPROCHE</li><li>PUBLICATIONS</li><li>CONTACT</li></ul>
  </nav>

  <section class="hero">
    <div class="hero-backdrop" role="img" aria-label="Vue floue d'une ville en arrière-plan"></div>
    <div class="hero-visual" role="img" aria-label="Cube blanc portant une croix rouge"></div>
    <h1 class="hero-title">Cabinet-conseil en communications et affaires publiques spécialisé dans le secteur de la santé.</h1>
    <div class="hero-cta">
      <span class="hero-cta-icon"><svg width="22" height="22" viewBox="0 0 22 22"><path d="M5 4l6 6 6-6M5 11l6 6 6-6" fill="none" stroke="#fff" stroke-width="3"/></svg></span>
      <span class="hero-cta-label">EN SAVOIR PLUS</span>
    </div>
  </section>

  <h2 class="section-title">Publication Récentes</h2>

  <footer class="site-footer"></footer>

  <div class="posts">
    <article class="post">
      <div class="post-media media-lab" role="img" aria-label="Personnel médical dans un laboratoire"></div>
      <h3 class="post-title">Titre de la publication</h3>
      <span class="post-date">23 juillet 2013</span>
      <p class="post-excerpt">Lorem ipsum dolor sit amet, consectetur adipisicing elit, sed do eiusmod tempor incididunt ut labore et dolore magna aliqua. Ut enim ad minim veniam, quis nostrud exercitation ullamco laboris nisi ut aliquip ex ea commodo consequat. Duis aute irure dolor in reprehenderit in voluptate velit esse cillum dolore eu fugiat nulla pariatur. Excepteur sint occaecat cupidatat non <em>proident, sunt in culpa</em> qui officia deserunt mollit anim id est Velit esse cillum dolore eu fugiat nulla pariatur. Excepteur sint occaecat cupidatat non proident, sunt in culpa qui officia deserunt mollit anim id est laborum.</p>
      <div class="post-more">Article complet <svg width="15" height="15" viewBox="0 0 15 15"><circle cx="7.5" cy="7.5" r="6.5" fill="none" stroke="#c8141c" stroke-width="1.4"/><path d="M4 7.5h6M7.5 4.8l2.7 2.7-2.7 2.7" fill="none" stroke="#c8141c" stroke-width="1.4"/></svg></div>
    </article>
    <article class="post">
      <div class="post-media media-flask" role="img" aria-label="Chercheur examinant une fiole"></div>
      <h3 class="post-title">Titre de la publication</h3>
      <span class="post-date">23 juillet 2013</span>
      <p class="post-excerpt">Lorem ipsum dolor sit amet, consectetur adipisicing elit, sed do eiusmod tempor incididunt ut labore et dolore magna aliqua. Ut enim ad minim veniam, quis nostrud exercitation ullamco laboris nisi ut aliquip ex ea commodo consequat. Duis aute irure dolor in reprehenderit in voluptate velit esse cillum dolore eu fugiat nulla pariatur. Excepteur sint occaecat cupidatat non <em>proident, sunt in culpa</em> qui officia deserunt mollit anim id est Velit esse <em>cillum dolore eu</em> fugiat nulla pariatur. Excepteur sint occaecat cupidatat non proident, sunt in culpa qui officia deserunt mollit anim id est laborum.</p>
      <div class="post-more">Article complet <svg width="15" height="15" viewBox="0 0 15 15"><circle cx="7.5" cy="7.5" r="6.5" fill="none" stroke="#c8141c" stroke-width="1.4"/><path d="M4 7.5h6M7.5 4.8l2.7 2.7-2.7 2.7" fill="none" stroke="#c8141c" stroke-width="1.4"/></svg></div>
    </article>
    <article class="post">
      <div class="post-media media-cross" role="img" aria-label="Cube blanc portant une croix rouge"></div>
      <h3 class="post-title">Titre de la publication</h3>
      <span class="post-date">23 juillet 2013</span>
      <p class="post-excerpt">Lorem ipsum dolor sit amet, consectetur adipisicing elit, sed do eiusmod tempor incididunt ut labore et dolore magna aliqua. Ut enim ad minim veniam, quis nostrud exercitation ullamco laboris nisi ut aliquip ex ea commodo consequat. Duis aute irure dolor in reprehenderit in voluptate velit esse cillum dolore eu fugiat nulla pariatur. Excepteur sint occaecat cupidatat non <em>proident, sunt in culpa</em> qui officia deserunt mollit anim id est Velit esse cillum dolore eu fugiat nulla pariatur. Excepteur sint occaecat cupidatat non proident, sunt in culpa qui officia deserunt mollit anim id est laborum.</p>
      <div class="post-more">Article complet <svg width="15" height="15" viewBox="0 0 15 15"><circle cx="7.5" cy="7.5" r="6.5" fill="none" stroke="#c8141c" stroke-width="1.4"/><path d="M4 7.5h6M7.5 4.8l2.7 2.7-2.7 2.7" fill="none" stroke="#c8141c" stroke-width="1.4"/></svg></div>
    </article>
    <article class="post">
      <div class="post-media media-doctors" role="img" aria-label="Équipe de médecins et d'infirmières"></div>
      <h3 class="post-title">Titre de la publication</h3>
      <span class="post-date">23 juillet 2013</span>
      <p class="post-excerpt">Lorem ipsum dolor sit amet, consectetur adipisicing elit, sed do eiusmod tempor incididunt ut labore et dolore magna aliqua. Ut enim ad minim veniam, quis nostrud exercitation ullamco laboris nisi ut aliquip ex ea commodo consequat. Duis aute irure dolor in reprehenderit in voluptate velit esse cillum dolore eu fugiat nulla pariatur. Excepteur sint occaecat cupidatat non <em>proident, sunt in culpa</em> qui officia deserunt mollit anim id est Velit esse <em>cillum dolore eu</em> fugiat nulla pariatur. Excepteur sint occaecat cupidatat non proident, sunt in culpa qui officia deserunt mollit anim id est laborum.</p>
      <div class="post-more">Article complet <svg width="15" height="15" viewBox="0 0 15 15"><circle cx="7.5" cy="7.5" r="6.5" fill="none" stroke="#c8141c" stroke-width="1.4"/><path d="M4 7.5h6M7.5 4.8l2.7 2.7-2.7 2.7" fill="none" stroke="#c8141c" stroke-width="1.4"/></svg></div>
    </article>
  </div>

  <div class="feed">
    <div class="feed-name">Chirpline <span class="feed-dot"></span></div>
    <p class="feed-text">Le Lorem Ipsum est simplement du faux texte employé dans la composition et la mise en page avant impression. Le Lorem Ipsum est le faux texte standard de.</p>
    <p class="feed-tags">#free #rebound&nbsp;it! #psd</p>
    <div class="feed-button">Chirp</div>
  </div>

  <form class="newsletter">
    <h4 class="newsletter-title">RECEVEZ NOS PUBLICATIONS</h4>
    <div class="newsletter-field">Votre nom</div>
    <div class="newsletter-field">Votre courriel</div>
    <div class="newsletter-submit">Abonnez-vous</div>
  </form>

  <div class="footer-rule"></div>
  <p class="copyright">(c) Solène Verbruggen. Tous droits réservés.</p>
</body>
</html>
```